Corporate website design needed

We need a Contemporary Industrial/Tech/Logistics Website design to match our logistic client's business. Our client consults and build logistics solutions that they manage but they are not a typical 3PL (3rd party logistics company) which is primarily engaged in moving boxes.
PSD file only for now, home and default templates.
COMPANY CHARACTER
DESIGN LOOK AND FEEL
• The design should also be modern and visually well organized — employing a combination of visual devices and info graphics. Keep it light and not too heavy but strong/ professional. And unique.
• The design should go beyond the typical industrial pick and pack 3PL representing [Logistics Company] as a High Tech/IT logistics company.
Some examples although these are not right for this client because they have much more content and present themselves more as a 3pl.
http://www.tg-gateway.example/ (More right then wrong - Like this but simplified)
http://www.morvanfreight.example (Ugly)
http://www.pdwellstead.example (More right then wrong but different focus)
http://www.halverinco.example/ Too 3PL trucking… We want a bit ore high level approach
The difference, the design should be a fusion in core concepts that culminate in a design which implies the following attributes. Tech (Big data / analytics / software), Consultancy (Solutions, SME, Leader), 3PL Industry vertical solutions.
NOTE: The visualization of “tech” is not “1” and “0”, but more “software and analytics” Perhaps more like www.quantelyx.example.
• They need to be seen as a solutions provider in Logistics and as in Subject matter experts
TONE
The tone needs to exude professionalism, expertise, though leadership along with technical and executional excellence.
Experienced
Knowledgeable
Confident
Determined
Straightforward
WEBSITE OBJECTIVES
• Focus C-Suite executives and logistics managers’ attention on [Logistics Company]s commanding knowledge and expertise, and unique approach to supply chain solutions producing more RFP wins
• Create an easy to scan design which decreases the reliance on text through featured text, summaries, and smaller “chunked” size bits of information.
• Convey [Logistics Company] as high-tech 3PL solutions developer and services provider with a ‘high-touch’ consultative approach.
• Showcase [Logistics Company]’s value propositions. (See Slider Content)
• Showcase [Logistics Company]’s expertise in logistical analytics.
• Gain recognition as an industry leader in evolutionary new space (supply chain 2.0)
WEBSITE STRATEGY
• Reduce reliance on text (at least within initial entry points for each section)
• Typography: Watch text line lengths and readability, bolder fonts. NO SERIFS
• Generally, create a click-through format so that users who want more details can find it, and those who don’t can get a snapshot without clicking through.
• Increase visual content through info graphics and some dynamic content, photography
• Better utilize the space on each page (e.g., add visual interest, photography and iconography where appropriate to break up copy blocks and maintain readable line lengths).
COLOR SCHEME
• Create a more engaging color scheme (the logo will remain the same under all circumstances).
• Red / grayscale may work…. Not too dark or heavy. Not too much red. Ex. parvixa.example
• Also try blues and greys. They seem to like that. Open to suggestions but don’t get to crazy. Red is in their logo but too much may be a problem.
PHOTOGRAPHY
Yes. And I will upload some.
If you pick photography please be sure to note Which stock house used and the image number!
CONTENT
The content will be presented in a more hierarchical format — with lead-ins, paragraph and section headers and navigational cues to expand lengthier content allowing the visitor to more easily scan the website. No case studies, No Social media, News while on the home page should not be over emphasized. They don't post a lot so it gets dated quickly ...
I will be uploading a wire frame and other elements.
NOTE: I uploaded my EXAMPLE mock up which is close but not close enough.
I am not a great designer. So I am looking for an alternative that exceed my design ability! These examples show the basic layout but I really want some varied alternatives.
The colors are inconsistent and type not quite right. The grey bar at top is not right and should probably go away.
Please pull the basic elements in the example together into a great design.
If you have questions please contact me.
i will upload some photography tomorrow that may be of use.
Thanks!
Updates
Hi All,
We are still evaluating the submitted designs. Sorry for the delay.
Target Market(s)
This website is primarily a validation website. Few new customers will search and find them as such...
The site should be Focused on C-Suite executives and logistics managers’ attention on [Logistics Company]s commanding knowledge and expertise, and unique approach to supply chain solutions producing more RFP wins
Industry/Entity Type
Business
Requirements
Must have
- Slide show, Clearly explain who they are and what they do.
Create an easy to scan design which decreases the reliance on text through featured text, summaries, and smaller “chunked” size bits of information.
Convey [Logistics Company] as high-tech 3PL solutions developer and services
provider with a ‘high-touch’ consultative approach.
Should not have
- No Ads space
No Social media
Not too cluttered. Keep it clean.

```html
<!DOCTYPE html>
<html lang="en">
<head>
<meta charset="utf-8">
<title>Northvane Logistics — Home</title>
<link href="https://fonts.googleapis.com/css2?family=Open+Sans:ital,wght@0,300;0,400;0,600;0,700;1,400&display=swap" rel="stylesheet">
<style>
:root{
  --page:#eceef1;
  --white:#ffffff;
  --red:#c8102e;
  --red-dark:#9e0c23;
  --ink:#34373c;
  --text:#6f7378;
  --muted:#9a9ea3;
  --blue:#1a9ad6;
  --blue-deep:#1f4f7a;
  --nav:#3f4246;
  --top:#2b2e32;
  --strip:#eeeff1;
  --band:#35383c;
  --foot:#45484c;
  --foot-out:#2c2f33;
  --foot-text:#a8acb0;
}
*{box-sizing:border-box;margin:0;padding:0}
html,body{width:1200px;height:2200px;overflow:hidden}
body{font-family:"Open Sans",Arial,sans-serif;background:var(--page);color:var(--text)}
.canvas{position:relative;width:1200px;height:2200px;overflow:hidden;background:var(--page)}
.abs{position:absolute}
a{color:inherit;text-decoration:none}

/* top */
.topbar{left:0;top:0;width:1200px;height:40px;background:var(--top)}
.top-strip{left:100px;top:0;width:1000px;height:40px;background:var(--strip)}
.top-links{right:125px;top:0;height:40px;display:flex;align-items:center;font-size:13px;color:var(--ink)}
.top-links span.sep{margin:0 18px;color:#888}
.header-red{left:0;top:40px;width:100px;height:155px;background:var(--red)}
.header{left:100px;top:40px;width:1000px;height:88px;background:var(--white)}
.brand{left:125px;top:58px;display:flex;align-items:center;gap:14px}
.brand-dot{width:50px;height:50px;border-radius:50%;background:var(--red)}
.brand-name{font-size:17px;font-weight:600;letter-spacing:6px;color:var(--ink);line-height:1.25}
.search{left:849px;top:65px;width:239px;height:36px;background:#dfe0e2;display:flex;align-items:center;justify-content:space-between;padding:0 10px;font-size:12px;font-style:italic;color:#9a9a9a}
.navbar{left:100px;top:128px;width:1000px;height:49px;background:var(--nav)}
.nav-red{left:0;top:128px;width:410px;height:67px;z-index:3}
.phone-num{left:177px;top:135px;font-size:22px;line-height:28px;color:#fff;z-index:4}
.phone-sub{left:177px;top:167px;font-size:12px;line-height:16px;color:#fff;z-index:4}
.nav-links{left:704px;top:128px;height:49px;display:flex;align-items:center;font-size:15px;font-weight:600;color:#fff}
.nav-links .sep{margin:0 14px;font-weight:400}

/* hero */
.hero{left:100px;top:177px;width:1000px;height:427px;background:linear-gradient(120deg,#3f9fd8 0%,#7cc4ec 45%,#cfe9f7 70%,#6fb7e2 100%)}
.hero-welcome{left:131px;top:306px;font-size:35px;color:#fff;font-weight:400}
.hero-name{left:131px;top:348px;font-size:40px;color:var(--blue-deep);font-weight:600}
.hero-caption{left:123px;top:409px;width:408px;height:72px;background:rgba(27,38,50,.88);padding:7px 10px}
.hero-caption h3{font-size:15px;color:#3cbcf0;font-weight:700}
.hero-caption p{font-size:14.5px;color:#fff;line-height:1.25}
.dots{left:1044px;top:581px;display:flex;gap:3px}
.dots i{width:8px;height:8px;border-radius:50%;background:#9aa6b0;display:block}
.dots i.on{background:var(--blue)}

/* intro */
.intro{left:100px;top:604px;width:1000px;height:269px;background:var(--white);text-align:center}
.intro h1{position:absolute;left:0;top:48px;width:1000px;font-size:22px;font-weight:600;color:var(--ink)}
.intro p{position:absolute;left:60px;top:92px;width:880px;font-size:14px;line-height:22px;color:var(--text)}
.btn{position:absolute;left:366px;top:165px;width:267px;height:40px;border:1px solid #c9cbce;border-radius:5px;box-shadow:0 2px 3px rgba(0,0,0,.15);font-size:13px;font-weight:600;color:var(--ink);line-height:38px;background:#fff}

/* services */
.services{left:100px;top:873px;width:1000px;height:427px;background:#f1f2f4}
.section-title{left:110px;top:893px;font-size:23px;font-weight:600;color:var(--ink)}
.rule{left:110px;top:953px;width:980px;height:1px;background:#c9ccd0}
.rule-accent{left:110px;top:951px;width:195px;height:5px;background:var(--blue)}
.service{top:1000px;width:230px;text-align:center}
.service svg{display:block;margin:0 auto}
.service h4{margin-top:10px;font-size:18.5px;font-weight:400;line-height:24px;color:var(--ink)}
.service.active h4{color:var(--blue)}
.service p{margin-top:8px;font-size:12px;line-height:18.5px;color:var(--text)}

/* news */
.news{left:100px;top:1300px;width:1000px;height:413px;background:var(--white)}
.col-title{top:1330px;font-size:20.5px;font-weight:600;color:var(--ink)}
.item{left:110px;width:290px;font-size:11.5px;line-height:20px;color:var(--muted)}
.item .hl{color:var(--blue)}
.item .date{color:var(--blue);font-style:italic}
.item p{margin-top:8px;width:275px;color:#888}
.divider{left:110px;top:1505px;width:270px;height:1px;background:#dcdee0}
.view-all{top:1633px;font-size:14px;font-style:italic;color:var(--ink)}
.thumb{left:449px;width:102px;height:100px;border:1px solid #dcdee0;background:#fff;padding:6px}
.thumb div{width:100%;height:100%}
.feat-text{left:560px;width:190px;font-size:13px;line-height:21px;color:var(--text)}
.feat-date{left:560px;font-size:9.5px;color:var(--muted);display:flex;align-items:center;gap:8px}
.video{left:786px;top:1389px;width:305px;height:160px;background:linear-gradient(135deg,#26303a,#5a6a76 50%,#2e3a44)}
.play{left:918px;top:1453px;width:42px;height:32px;background:rgba(0,0,0,.6);border-radius:3px}
.video-text{left:786px;top:1560px;width:310px;font-size:13px;line-height:20.5px;color:var(--text)}

/* footer band */
.band{left:0;top:1728px;width:1200px;height:103px;background:var(--band)}
.tw-dot{left:126px;top:1764px;width:22px;height:22px;border-radius:50%;background:#5b5f64}
.tweet{left:197px;top:1757px;width:430px;font-size:13px;line-height:22px;font-style:italic;color:#9ea2a6}
.tweet .hl{color:var(--blue)}
.news-red{left:0;top:0}
.nl-title{left:820px;top:1741px;font-size:16px;font-weight:700;color:#fff}
.nl-input{left:820px;top:1775px;width:219px;height:28px;background:var(--red-dark);font-size:12px;color:#f3d5da;padding:6px 10px}
.nl-go{left:1049px;top:1775px;width:37px;height:28px;background:var(--red-dark);font-size:12px;color:#fff;text-align:center;line-height:28px}

/* footer */
.foot-out{left:0;top:1875px;width:1200px;height:325px;background:var(--foot-out)}
.foot{left:100px;top:1831px;width:1000px;height:318px;background:var(--foot)}
.fcol{top:1862px}
.fcol h5{font-size:14.5px;font-weight:400;color:#dfe1e3;display:flex;align-items:center;gap:14px}
.fcol h5::after{content:"";width:60px;height:1px;background:#62666b;display:block}
.fcol ul{list-style:none;margin-top:17px}
.fcol li{font-size:13px;line-height:20.1px;color:var(--foot-text)}
.foot-brand{left:129px;top:2080px;display:flex;align-items:center;gap:14px}
.foot-brand .brand-dot{width:40px;height:40px;background:#5d6166}
.foot-brand .brand-name{color:#8d9196;font-size:15px}
.bottom{left:100px;top:2149px;width:1000px;height:51px;background:#383b3f;font-size:12.5px;color:var(--foot-text)}
.bottom .l{position:absolute;left:22px;top:16px}
.bottom .r{position:absolute;right:26px;top:16px}
.bottom .sep{margin:0 14px}
</style>
</head>
<body>
<div class="canvas">

  <!-- top bar -->
  <div class="abs topbar"></div>
  <div class="abs top-strip"></div>
  <svg class="abs" style="left:715px;top:0" width="385" height="40"><polygon points="0,0 385,0 385,40 20,40" fill="#e3e4e7"/></svg>
  <nav class="abs top-links">
    <a>Home</a><span class="sep">|</span><a>Company</a><span class="sep">|</span><a>Careers</a><span class="sep">|</span><a>Contact Us</a>
  </nav>

  <!-- header -->
  <div class="abs header-red"></div>
  <div class="abs header"></div>
  <div class="abs brand">
    <span class="brand-dot"></span>
    <span class="brand-name">NORTHVANE<br>LOGISTICS</span>
  </div>
  <div class="abs search">
    <span>Search here...</span>
    <svg width="18" height="18" viewBox="0 0 18 18"><circle cx="7" cy="7" r="5.5" fill="none" stroke="#9a9a9a" stroke-width="2"/><line x1="11" y1="11" x2="16" y2="16" stroke="#9a9a9a" stroke-width="2.5"/></svg>
  </div>

  <div class="abs navbar"></div>

  <!-- hero -->
  <div class="abs hero" role="img" aria-label="Photo of a businesswoman touching a glowing data interface over a world map, charts and sky"></div>
  <div class="abs hero-welcome">Welcome To</div>
  <div class="abs hero-name">Northvane Logistics</div>
  <div class="abs hero-caption">
    <h3>ABOUT SUPPLY CHAIN TRANSFORMATION</h3>
    <p>Lorem &nbsp;ipsum dolor sit amet consectetur adipsicing elit, sed do euismod tempor incidunt manga aliqua..</p>
  </div>
  <div class="abs dots"><i class="on"></i><i></i><i></i><i></i></div>

  <!-- phone tab, layered over the hero top -->
  <svg class="abs nav-red" width="410" height="67" viewBox="0 0 410 67">
    <polygon points="0,0 403,0 378,67 0,67" fill="#c8102e"/>
    <circle cx="142" cy="33" r="22" fill="none" stroke="#e8a0ab" stroke-width="1.5"/>
    <path d="M133 26 q2-3 5-1 l3 4 q1 2-1 3 l-2 1 q2 5 7 7 l1-2 q1-2 3-1 l4 3 q2 3-1 5 q-4 3-9 0 q-8-5-11-12 q-2-5 1-7z" fill="#fff"/>
  </svg>
  <div class="abs phone-num">1-800-555-0142</div>
  <div class="abs phone-sub">24/7 Toll Free Call Us Now</div>
  <nav class="abs nav-links"><a>SOLUTIONS</a><span class="sep">|</span><a>OUR PROCESS</a><span class="sep">|</span><a>INDUSTRIES</a></nav>

  <!-- intro -->
  <section class="abs intro">
    <h1>NORTHVANE LOGISTICS THE BEST SOLUTIONS PROVIDERS</h1>
    <p>Northvane transforms supply chains by managing complexity, providing data-driven insights and implementing foweard-thinking innovation and actionable strategies that change business results..</p>
    <a class="btn">THE BEST SOLUTIONS PROVIDERS</a>
  </section>

  <!-- services -->
  <section class="abs services"></section>
  <h2 class="abs section-title">OUR SERVICES</h2>
  <div class="abs rule"></div>
  <div class="abs rule-accent"></div>

  <div class="abs service active" style="left:92px">
    <svg width="94" height="100" viewBox="0 0 94 100">
      <polygon points="47,3 88,26 88,74 47,97 6,74 6,26" fill="#1aa0dc"/>
      <path d="M27 70 V46 l10 -6 v6 l10 -6 v6 l10 -6 V30 h6 v40z" fill="#fff"/>
      <rect x="31" y="54" width="5" height="5" fill="#1aa0dc"/><rect x="40" y="54" width="5" height="5" fill="#1aa0dc"/><rect x="49" y="54" width="5" height="5" fill="#1aa0dc"/>
    </svg>
    <h4>Material Management<br>&amp; Factory Support</h4>
    <p>Lorem ipsum dolor sit amet, adipis-<br>icing elit, sed do eiusmod tempor<br>incididunt magna aliqua..</p>
  </div>
  <div class="abs service" style="left:354px">
    <svg width="94" height="100" viewBox="0 0 94 100">
      <polygon points="47,5 86,27 86,73 47,95 8,73 8,27" fill="none" stroke="#34373c" stroke-width="3"/>
      <path d="M28 38 h7 l5 18 h20 l4 -13 h-27" fill="none" stroke="#34373c" stroke-width="3.5" stroke-linejoin="round"/>
      <circle cx="42" cy="63" r="3.5" fill="#34373c"/><circle cx="57" cy="63" r="3.5" fill="#34373c"/>
    </svg>
    <h4>Retail &amp; E-commerce<br>Distribution</h4>
    <p>Lorem ipsum dolor sit amet, adipis-<br>icing elit, sed do eiusmod tempor<br>incididunt magna aliqua..</p>
  </div>
  <div class="abs service" style="left:616px">
    <svg width="94" height="100" viewBox="0 0 94 100">
      <polygon points="47,5 86,27 86,73 47,95 8,73 8,27" fill="none" stroke="#34373c" stroke-width="3"/>
      <line x1="33" y1="36" x2="62" y2="65" stroke="#34373c" stroke-width="5" stroke-linecap="round"/>
      <line x1="62" y1="35" x2="32" y2="65" stroke="#34373c" stroke-width="5" stroke-linecap="round"/>
      <circle cx="62" cy="35" r="6" fill="none" stroke="#34373c" stroke-width="3"/>
    </svg>
    <h4>After Market<br>Support</h4>
    <p>Lorem ipsum dolor sit amet, adipis-<br>icing elit, sed do eiusmod tempor<br>incididunt magna aliqua..</p>
  </div>
  <div class="abs service" style="left:877px">
    <svg width="94" height="100" viewBox="0 0 94 100">
      <polygon points="47,5 86,27 86,73 47,95 8,73 8,27" fill="none" stroke="#34373c" stroke-width="3"/>
      <circle cx="40" cy="54" r="10" fill="none" stroke="#34373c" stroke-width="6" stroke-dasharray="4 2.5"/>
      <circle cx="40" cy="54" r="4" fill="#34373c"/>
      <circle cx="57" cy="40" r="7" fill="none" stroke="#34373c" stroke-width="5" stroke-dasharray="3 2"/>
      <circle cx="58" cy="62" r="6" fill="none" stroke="#34373c" stroke-width="4" stroke-dasharray="3 2"/>
    </svg>
    <h4>Critical<br>Logistics</h4>
    <p>Lorem ipsum dolor sit amet, adipis-<br>icing elit, sed do eiusmod tempor<br>incididunt magna aliqua..</p>
  </div>

  <!-- news -->
  <section class="abs news"></section>
  <h3 class="abs col-title" style="left:109px">Recent News</h3>
  <h3 class="abs col-title" style="left:449px">Featured News</h3>
  <h3 class="abs col-title" style="left:783px">The Northvane Difference</h3>

  <div class="abs item" style="top:1393px">
    Corwen Ridge Marlborough Sauvignon <span class="hl">Blanced etc</span><br>
    <span class="date">posted on March 13, 2014 20:15</span>
    <p>Media release; summer has never tasted better than with Corwen Ridge's 2014 Sauvignon Blanc</p>
  </div>
  <div class="abs divider"></div>
  <div class="abs item" style="top:1524px">
    Corwen Ridge Marlborough Sauvignon <span class="hl">Blanced etc</span><br>
    <span class="date">posted on March 13, 2014 20:15</span>
    <p>Media release; summer has never tasted better than with Corwen Ridge's 2012 Sauvignon Blanc</p>
  </div>
  <a class="abs view-all" style="left:114px">View All</a>

  <div class="abs thumb" style="top:1397px"><div role="img" aria-label="Photo of a woman reading a tablet" style="background:linear-gradient(135deg,#2a1d18,#8a5a44 60%,#d8b9a4)"></div></div>
  <div class="abs feat-text" style="top:1405px">This in one of the important Blog Post of this website.</div>
  <div class="abs feat-date" style="top:1461px"><svg width="12" height="12"><rect x="1" y="2" width="10" height="9" fill="none" stroke="#b5b8bb"/><line x1="1" y1="5" x2="11" y2="5" stroke="#b5b8bb"/></svg>25, JAN, 2011</div>
  <div class="abs thumb" style="top:1518px"><div role="img" aria-label="Black and white photo of colleagues in a meeting" style="background:linear-gradient(135deg,#3a3a3a,#9c9c9c 55%,#e0e0e0)"></div></div>
  <div class="abs feat-text" style="top:1526px">This in one of the important Blog Post of this website.</div>
  <div class="abs feat-date" style="top:1582px"><svg width="12" height="12"><rect x="1" y="2" width="10" height="9" fill="none" stroke="#b5b8bb"/><line x1="1" y1="5" x2="11" y2="5" stroke="#b5b8bb"/></svg>25, JAN, 2011</div>
  <a class="abs view-all" style="left:456px">View All</a>

  <div class="abs video" role="img" aria-label="Video still of two engineers working in a server room"></div>
  <div class="abs play"><svg width="42" height="32"><polygon points="17,9 28,16 17,23" fill="#fff"/></svg></div>
  <p class="abs video-text">Lorem ipsum dolor sit amet, consectetur adipis-icing elit, sed do eiusmod tempor incididunt ut labore et dolore magna aliqua.</p>
  <a class="abs view-all" style="left:789px">View All</a>

  <!-- footer band -->
  <div class="abs band"></div>
  <span class="abs tw-dot"></span>
  <p class="abs tweet"><span class="hl">@MaraDellwyn</span> &nbsp;no, it's the default one when you go to tools &gt; import &gt; blogpress the first one in line <span class="hl">3 days ago</span></p>
  <svg class="abs news-red" width="1200" height="1880" viewBox="0 0 1200 1880" style="pointer-events:none">
    <polygon points="670,1831 755,1716 1200,1716 1200,1875 1100,1875 1100,1831" fill="#c8102e"/>
    <circle cx="767" cy="1772" r="27" fill="#9e0c23"/>
    <path d="M755 1768 l12 -9 l12 9 v13 h-24z" fill="none" stroke="#fff" stroke-width="2"/>
    <path d="M755 1768 l12 8 l12 -8" fill="none" stroke="#fff" stroke-width="2"/>
  </svg>
  <div class="abs nl-title">Newsletter Sign Up</div>
  <div class="abs nl-input">your email address</div>
  <div class="abs nl-go">Go</div>

  <!-- footer -->
  <div class="abs foot-out"></div>
  <div class="abs foot"></div>
  <div class="abs fcol" style="left:123px"><h5>Our Process</h5>
    <ul><li>Concept of operations</li><li>Supplying the infrastructure</li><li>Analyzing the data</li><li>Managing Complexity</li><li>Providing actionable stratrgies</li><li>nvesting in our clients sucess</li><li>Driving business results</li></ul></div>
  <div class="abs fcol" style="left:387px"><h5>Our Solutions</h5>
    <ul><li>Business Analytics</li><li>Geigraphical Coverage</li><li>Project Financing</li><li>Project Implementation</li><li>Technology</li><li>Quality</li></ul></div>
  <div class="abs fcol" style="left:650px"><h5>Industries We Serve</h5>
    <ul><li>Aerospace</li><li>Defense</li><li>Industrial</li><li>Manifacturing</li><li>Media &amp; Entertainment</li><li>Medical</li><li>Retail</li><li>Telecom &amp; Electronics</li></ul></div>
  <div class="abs fcol" style="left:914px"><h5>Company</h5>
    <ul><li>Culture</li><li>Community Involvement</li><li>Major Metro Presence</li><li>News</li><li>Carreers</li><li>Contact</li></ul></div>
  <div class="abs foot-brand"><span class="brand-dot"></span><span class="brand-name">NORTHVANE<br>LOGISTICS</span></div>

  <div class="abs bottom">
    <div class="l">Solutions<span class="sep">|</span>Our Process<span class="sep">|</span>Industries</div>
    <div class="r">© NORTHVANE, INC. 2014 &nbsp; Privacy Policy<span class="sep">|</span>Term of Use</div>
  </div>

</div>
</body>
</html>
```